Quopath Cell Phone Repair

We are a small cell phone repair store in need of a redesign to our current business card to make it a more modern, cleaner design that will catch folks' attention (perhaps with rounded edges ) - But still include most of the information listed on the current card. Would like to keep the current color scheme of black/white and green. Card will not need any personnel name included. Would like to see some designs include takes on a velmora or zentab screen as well as more traditional cards.

Target Market(s)

broad spectrum across all cell phone users

Industry/Entity Type

Cell Phone

Contact Information for Business Card

changes to front text:
keep business Logo
business address, phone number website and email. All other info optional (add chatterly and glimmo icons on card

Rear of card:

Keep repair services, change zentab repair to korslate repair, change brevix os repair to data recovery (with appropriate icon or substitute)
remove products text
remove wbq and delvo from manufacturer logos, add fenwicka.

Requirements
Must have
• business Logo
• business address, phone number website and email
• keep colors to white/black/green/gray
• chatterly and glimmo icons on card
Nice to have
• Would like to see 'traditional' business card design as well as creative design incorporating incorporating front of cell phone (eg zentab or brevix). Rounded edges would be nice but not necessary.

```html
<!DOCTYPE html>
<html lang="en">
<head>
<meta charset="utf-8">
<title>Quopath Cell Phone Repair – Business Card</title>
<link rel="stylesheet" href="https://fonts.googleapis.com/css2?family=Oswald:wght@300;400;600;700&family=Cabin:wght@500&display=swap">
<style>
  :root {
    --green: #6ab04c;
    --green-dark: #3f8a35;
    --ink: #231f20;
    --white: #ffffff;
    --band: #c9c9c9;
    --band-text: #333333;
    --edge: #b5b5b5;
    --mark: #1a1a1a;
  }
  * { margin: 0; padding: 0; box-sizing: border-box; }
  html, body { width: 1200px; height: 820px; overflow: hidden; background: var(--white); }
  .sheet { position: relative; width: 1200px; height: 820px; }
  .art { position: absolute; left: 0; top: 0; }
  .t { position: absolute; white-space: nowrap; }

  .brand-name { left: 190px; top: 186px; width: 242px; text-align: right; font: 700 64px/1 "Oswald", sans-serif; color: var(--ink); letter-spacing: 1px; }
  .brand-tag { left: 190px; top: 283px; width: 242px; text-align: right; font: 700 25px/1 "Oswald", sans-serif; color: var(--ink); }
  .service-band { left: 105px; top: 333px; width: 338px; text-align: center; font: 600 12px/16px "Oswald", sans-serif; color: var(--band-text); }
  .contact { left: 157px; font: 500 14.5px/1 "Cabin", sans-serif; color: var(--ink); }
  .social { left: 157px; font: 500 14.5px/1 "Cabin", sans-serif; color: var(--green-dark); }

  .services-title { left: 876px; top: 147px; width: 100px; text-align: center; font: 700 19px/1 "Oswald", sans-serif; color: var(--white); }
  .tile-label { width: 120px; text-align: center; font: 300 15px/1 "Oswald", sans-serif; }
  .on-light { color: var(--ink); }
  .on-dark { color: var(--white); }
  .maker { font: 600 19px/1 "Oswald", sans-serif; color: var(--ink); }
  .products { left: 757px; top: 529px; font: 300 14.5px/19.2px "Oswald", sans-serif; color: var(--white); }
  .products strong { font-weight: 600; }
</style>
</head>
<body>
<main class="sheet">
  <svg class="art" width="1200" height="820" viewBox="0 0 1200 820" aria-hidden="false">
    <defs>
      <clipPath id="back-face"><rect x="735" y="74" width="382" height="670" rx="22"/></clipPath>
      <g id="reg-mark" fill="none" stroke="var(--mark)" stroke-width="1">
        <circle r="12"/><circle r="7" fill="var(--mark)"/>
        <line x1="-20" y1="0" x2="20" y2="0"/><line x1="0" y1="-20" x2="0" y2="20"/>
      </g>
      <linearGradient id="photo-grey" x1="0" y1="0" x2="0" y2="1">
        <stop offset="0" stop-color="#e6e6e6"/><stop offset="1" stop-color="#7c7c7c"/>
      </linearGradient>
      <linearGradient id="photo-water" x1="0" y1="0" x2="0" y2="1">
        <stop offset="0" stop-color="#dfe6ea"/><stop offset="1" stop-color="#3f7fa8"/>
      </linearGradient>
      <linearGradient id="photo-dark" x1="0" y1="0" x2="0" y2="1">
        <stop offset="0" stop-color="#5a4a40"/><stop offset="1" stop-color="#1e1a18"/>
      </linearGradient>
      <linearGradient id="photo-warm" x1="0" y1="0" x2="1" y2="1">
        <stop offset="0" stop-color="#d9dde3"/><stop offset="1" stop-color="#b98b72"/>
      </linearGradient>
    </defs>

    <!-- print marks -->
    <g class="crop-marks" stroke="var(--mark)" stroke-width="0.8">
      <line x1="83" y1="0" x2="83" y2="48"/><line x1="465" y1="0" x2="465" y2="48"/>
      <line x1="83" y1="772" x2="83" y2="820"/><line x1="465" y1="772" x2="465" y2="820"/>
      <line x1="10" y1="74" x2="56" y2="74"/><line x1="10" y1="744" x2="56" y2="744"/>
      <line x1="492" y1="74" x2="538" y2="74"/><line x1="492" y1="744" x2="538" y2="744"/>
      <line x1="735" y1="0" x2="735" y2="48"/><line x1="1117" y1="0" x2="1117" y2="48"/>
      <line x1="735" y1="772" x2="735" y2="820"/><line x1="1117" y1="772" x2="1117" y2="820"/>
      <line x1="662" y1="74" x2="708" y2="74"/><line x1="662" y1="744" x2="708" y2="744"/>
      <line x1="1144" y1="74" x2="1190" y2="74"/><line x1="1144" y1="744" x2="1190" y2="744"/>
    </g>
    <g class="registration-marks">
      <use href="#reg-mark" x="274" y="18"/><use href="#reg-mark" x="274" y="800"/>
      <use href="#reg-mark" x="19" y="409"/><use href="#reg-mark" x="529" y="409"/>
      <use href="#reg-mark" x="927" y="18"/><use href="#reg-mark" x="927" y="800"/>
      <use href="#reg-mark" x="671" y="409"/><use href="#reg-mark" x="1181" y="409"/>
    </g>

    <!-- front: phone body -->
    <g class="card-front">
      <rect x="58" y="50" width="432" height="719" rx="50" fill="var(--white)" stroke="var(--edge)" stroke-width="1"/>
      <rect x="83" y="74" width="382" height="670" rx="22" fill="var(--ink)"/>
      <circle cx="182" cy="105" r="8" fill="var(--white)"/>
      <rect x="236" y="101" width="75" height="9" rx="4.5" fill="var(--white)"/>
      <rect x="357" y="102" width="16" height="8" rx="4" fill="var(--white)"/>

      <rect x="105" y="139" width="338" height="513" fill="var(--white)"/>
      <circle class="brand-mark" cx="150" cy="245" r="34" fill="var(--green)"/>
      <rect x="105" y="328" width="338" height="41" fill="var(--band)"/>
      <rect x="105" y="369" width="338" height="283" fill="var(--green)"/>

      <g class="contact-rows">
        <rect x="125" y="378" width="312" height="32" rx="8" fill="var(--white)"/>
        <rect x="125" y="425" width="312" height="32" rx="8" fill="var(--white)"/>
        <rect x="125" y="472" width="312" height="32" rx="8" fill="var(--white)"/>
        <rect x="125" y="519" width="312" height="32" rx="8" fill="var(--white)"/>
        <rect x="125" y="564" width="312" height="32" rx="8" fill="var(--white)"/>
        <rect x="125" y="610" width="312" height="32" rx="8" fill="var(--white)"/>
        <g fill="var(--green)" stroke="#e9e9e9" stroke-width="4">
          <circle cx="131" cy="394" r="17"/><circle cx="131" cy="441" r="17"/>
          <circle cx="131" cy="488" r="17"/><circle cx="131" cy="535" r="17"/>
          <circle cx="131" cy="580" r="17"/><circle cx="131" cy="626" r="17"/>
        </g>
        <!-- pin -->
        <path d="M131 385a7 7 0 0 1 7 7c0 5-7 12-7 12s-7-7-7-12a7 7 0 0 1 7-7z" fill="var(--white)"/>
        <circle cx="131" cy="392" r="2.6" fill="var(--green)"/>
        <!-- phone -->
        <path d="M122 442c0-4 4-6 9-6s9 2 9 6v2h-5v-2.5c-2-.8-6-.8-8 0v2.5h-5z" fill="var(--white)"/>
        <!-- globe -->
        <g fill="none" stroke="var(--white)" stroke-width="1.8">
          <circle cx="131" cy="488" r="9"/><ellipse cx="131" cy="488" rx="4" ry="9"/>
          <line x1="122" y1="488" x2="140" y2="488"/>
        </g>
        <text x="131" y="541" text-anchor="middle" font-family="Cabin, sans-serif" font-size="18" font-weight="500" fill="var(--white)">@</text>
      </g>

      <rect x="124" y="690" width="15" height="10" fill="none" stroke="var(--white)" stroke-width="2"/>
      <rect x="248" y="677" width="53" height="33" rx="5" fill="none" stroke="var(--white)" stroke-width="3"/>
      <path d="M388 690h10a4 4 0 0 1 0 8h-10M391 686l-4 4 4 4" fill="none" stroke="var(--white)" stroke-width="2"/>
    </g>

    <!-- back -->
    <g class="card-back">
      <rect x="710" y="50" width="432" height="719" rx="50" fill="var(--white)" stroke="var(--edge)" stroke-width="1"/>
      <g clip-path="url(#back-face)">
        <rect x="735" y="74" width="382" height="670" fill="var(--white)"/>
        <polygon points="805,74 1117,74 1117,435" fill="var(--ink)"/>
        <polygon points="735,382 735,744 1047,744" fill="var(--ink)"/>
      </g>
      <circle cx="890" cy="111" r="7" fill="var(--white)"/>
      <circle cx="927" cy="111" r="15" fill="var(--white)" stroke="#b8b8b8" stroke-width="3"/>
      <line x1="774" y1="159" x2="877" y2="159" stroke="#9a9a9a" stroke-width="1"/>
      <line x1="974" y1="159" x2="1077" y2="159" stroke="#9a9a9a" stroke-width="1"/>

      <g class="service-tiles" stroke="var(--green)" stroke-width="4">
        <rect x="772" y="184" width="86" height="86" rx="10" fill="url(#photo-grey)" role="img" aria-label="Phone with a cracked screen"/>
        <rect x="884" y="184" width="86" height="86" rx="10" fill="url(#photo-water)" role="img" aria-label="Phone splashing into water"/>
        <rect x="996" y="184" width="86" height="86" rx="10" fill="url(#photo-grey)" role="img" aria-label="Close-up of a charging port"/>
        <rect x="772" y="302" width="86" height="86" rx="10" fill="url(#photo-grey)" role="img" aria-label="Opened hard drive platter"/>
        <rect x="884" y="302" width="86" height="86" rx="10" fill="url(#photo-dark)" role="img" aria-label="Phone screen with an unlocked padlock"/>
        <rect x="996" y="302" width="86" height="86" rx="10" fill="url(#photo-warm)" role="img" aria-label="Hands using a tablet"/>
      </g>

      <rect x="889" y="696" width="74" height="9" rx="4.5" fill="var(--white)"/>
      <line x1="895" y1="700.5" x2="957" y2="700.5" stroke="#777" stroke-width="1.5" stroke-dasharray="1.5 1.5"/>
    </g>
  </svg>

  <!-- front text -->
  <div class="t brand-name">QUOPATH</div>
  <div class="t brand-tag">CELL PHONE REPAIR</div>
  <div class="t service-band">Unlocking &amp; Flashing Services | Smart Phones &amp; Accessories<br>Water Damage Repair | Screen Repair</div>
  <div class="t contact" style="top:387px">1480 Harbor Row, Lakemont MD 20910</div>
  <div class="t contact" style="top:434px">555.014.2268</div>
  <div class="t contact" style="top:481px">www.quopathstore.com</div>
  <div class="t contact" style="top:528px">info@quopath.com</div>
  <div class="t social" style="top:573px">chatterly</div>
  <div class="t social" style="top:619px">glimmo</div>

  <!-- back text -->
  <div class="t services-title">SERVICES</div>
  <div class="t tile-label on-light" style="left:755px;top:274px">Cracked Screen</div>
  <div class="t tile-label on-light" style="left:867px;top:274px">Water Damage</div>
  <div class="t tile-label on-dark" style="left:979px;top:274px">Charging Port</div>
  <div class="t tile-label on-light" style="left:755px;top:394px">Data Recovery</div>
  <div class="t tile-label on-light" style="left:867px;top:394px">Cell Phone Unlock</div>
  <div class="t tile-label on-dark" style="left:979px;top:394px">korslate repair</div>

  <div class="t maker" style="left:872px;top:444px">Corvane</div>
  <div class="t maker" style="left:929px;top:485px">zentab</div>
  <div class="t maker" style="left:950px;top:530px">velmora</div>
  <div class="t maker" style="left:990px;top:586px">Lumiq</div>
  <div class="t maker" style="left:1034px;top:632px">fenwicka</div>

  <div class="t products"><strong>Products :</strong><br>Bluetooth Headsets,<br>Wall &amp; Car Charges,<br>Powercell pack chargers,<br>Batteries,<br>Screen Protectors,<br>Harborshell,<br>Eco Friendly Cases,<br>Waterproof Cases,<br>Stereo Headsets</div>
</main>
</body>
</html>
```